BrightKestrel - IT Consultancy Website

Our company is called BrightKestrel and our purpose is to help companies sustainably embrace and reap the benefits of cloud platforms, through transforming practices, skills and technology using DevOps and Security practices such that they are able to automate, manage and secure their cloud platforms to deliver product to market with increasing velocity.

To get our business started I require a website that will model the typical layout of an IT consultancy services company to an Australian Market. There are many examples of such a site, here are some of them. We would like a landing page and then a few simple menu options (About, Blog, Services etc..) to additional content

http://morvane.com.au/
http://www.pellixa.com.au/
http://www.tarno.com.au/

I require the site to be created with a separate CSS file that maintains the colour palette. This is a very important requirement, I want to be able to change the colours employed in the site in a single location and not have to scan through multiple files to replace the codes.

The website must be built using static content as it will not be hosted on a web server but instead in NBX using V7 and Pathwave CDN. Therefore please stick to HTML, JavaScript, CSS and other static file formats. The website needs to be response, smooth and reactive. It should render on desktop, mobile and tablet and feature smooth scrolling, transitions and fade in's.

The website should give the customer confidence that they are dealing with a highly professional IT services company, focused strongly on cloud (NBX, Kentrel Vista, Orvane Hub etc..), motivated by beautiful and fluid design.

In order to make this simpler for you, the designer, I have already purchased this template from https://quillframe.com/theme/northgate-versatile-layout-QX7K31904 and uploaded it. Feel free to use this template if you choose (note that it makes use of a separate color palette which is a key requirement) or use one of your own choosing. If you do use this template ensure that it does not look too much like "another bootstrap site" therefore use the layout and widgets but make the site look fresh and original too.
Obviously you must delete all trace of the bootstrap package once the project has completed if you do use it

Target Market(s)

Corporate and medium enterprise businesses

Industry/Entity Type

Information Technology

Coding

Coded - Design and coding required

Number of Pages Required

4 page

Font styles to use
Sans Serif

Colors
abd036
33a6d7

Requirements
Must have
• The website should give the customer confidence that they are dealing with a highly professional IT services company, focused strongly on cloud (NBX, Kentrel Vista, Orvane Hub etc..), motivated by beautiful and fluid design. Our company name is BrightKestrel, the site needs to pay homage to the themes of fluidity and logic
• Along with About Us, Services and a Blog page could I also get social logo's included too
Nice to have
• The website must be built using static content as it will not be hosted on a web server but instead in NBX using V7 and Pathwave CDN. Therefore please stick to HTML, JavaScript, CSS and other static file formats. The website needs to be response, smooth and reactive. It should render on desktop, mobile and tablet and feature smooth scrolling, transitions and fade in's.
Should not have
• Lurid colours, or too much animations. The design must "flow"

```html
<!DOCTYPE html>
<html lang="en">
<head>
<meta charset="utf-8">
<title>BrightKestrel – Cloud Infrastructure Security</title>
<link href="https://fonts.googleapis.com/css2?family=Roboto:wght@300;400;500;700&family=Reenie+Beanie&display=swap" rel="stylesheet">
<style>
:root{
  --blue:#33a6d7;
  --blue-dark:#2e9ac9;
  --navy:#1d2945;
  --ring:#2271ab;
  --green:#abd036;
  --ink:#2b2b2b;
  --muted:#666b72;
  --mist:#e8eaef;
  --sky:#def0f6;
  --card:#f7f8fa;
  --placeholder:#bdbdbd;
  --white:#ffffff;
}
*{box-sizing:border-box;margin:0;padding:0}
html,body{width:1200px;height:2429px;overflow:hidden}
body{font-family:'Roboto',sans-serif;color:var(--ink);background:var(--white);position:relative}
section,header,footer{position:relative;width:1200px}

/* top bar */
.topbar{height:33px;background:var(--blue);color:var(--white);font-size:13px;display:flex;align-items:center;padding:0 52px}
.topbar .contact{display:flex;gap:30px}
.topbar .contact span{display:flex;align-items:center;gap:8px}
.topbar .right{margin-left:auto;display:flex;align-items:center;gap:18px}
.social-dot{width:12px;height:12px;border-radius:2px;background:rgba(255,255,255,.85)}

/* nav */
.navbar{height:71px;background:#dcedf5;display:flex;align-items:center;padding:0 52px}
.brand{font-size:38px;font-weight:500;color:var(--blue);letter-spacing:-.5px}
.menu{margin-left:auto;display:flex;gap:38px;font-size:15px;color:#333;text-transform:uppercase}

/* hero */
.hero{height:547px;background:var(--navy);overflow:hidden}
.globe{position:absolute;left:16px;top:51px;width:444px;height:444px;border-radius:50%;
  background:radial-gradient(circle at 50% 50%,rgba(51,166,215,.05),rgba(51,166,215,.28) 70%,rgba(51,166,215,.05) 72%,transparent 73%)}
.hero-copy{position:absolute;left:440px;width:760px;top:104px;text-align:center;color:var(--white)}
.hero-title{font-family:'Reenie Beanie',cursive;font-weight:400;font-size:92px;line-height:80px;letter-spacing:1px;white-space:nowrap}
.hero-sub{font-size:21px;font-weight:500;margin-top:30px}
.hero-actions{display:flex;justify-content:center;align-items:center;gap:22px;margin-top:28px}
.btn{display:inline-flex;align-items:center;justify-content:center;height:36px;padding:0 6px;font-size:10px;font-weight:700;text-transform:uppercase;border-radius:3px;white-space:nowrap}
.btn-primary{background:var(--blue);color:var(--white);width:94px}
.btn-ghost{border:1.5px solid var(--white);color:var(--white);width:106px}
.badge{width:74px;height:38px;background:var(--white)}

/* about */
.about{height:275px;background:linear-gradient(180deg,#edeef2,#e3e6ec)}
.section-title{text-align:center;font-size:21px;font-weight:500;color:#2a2a2a}
.rule{position:absolute;left:42px;right:42px;border-top:1.5px dotted var(--blue)}
.about .section-title{padding-top:27px}
.about .rule{top:65px}
.about p{position:absolute;top:120px;left:60px;right:60px;text-align:center;font-size:13px;line-height:20px;color:var(--muted)}

/* services */
.services{height:317px;background:linear-gradient(180deg,#70baf0 0%,#b9dcf6 38%,#eef7fd 58%,#ffffff 100%);overflow:hidden}
.services .section-title{padding-top:25px}
.services .rule{top:63px}
.service{position:absolute;top:105px;width:400px;text-align:center}
.service .icon{width:76px;height:81px;margin:0 auto;background:var(--blue);display:flex;align-items:center;justify-content:center}
.service h3{font-size:17px;font-weight:500;margin-top:21px}
.service p{font-size:13px;line-height:19.5px;color:var(--muted);margin:18px auto 0;width:330px}

/* blog */
.blog{height:983px;background:var(--sky)}
.blog .section-title{padding-top:8px}
.blog .rule{top:46px;left:52px;right:52px}
.cards{position:absolute;top:104px;left:52px;display:flex;gap:30px}
.card{width:251px;height:353px;background:var(--card)}
.card .thumb{height:186px;background:var(--placeholder);display:flex;align-items:center;justify-content:center;font-size:31px;color:#111}
.card .body{padding:0 17px}
.card h4{font-size:17px;font-weight:700;margin-top:16px}
.card p{font-size:13px;line-height:19.5px;color:var(--muted);margin-top:8px;height:60px}
.card .meta{border-top:1px dotted #c9ccd1;margin-top:14px;padding-top:12px;display:flex;justify-content:space-between;font-size:11px;color:#555}
.view-more{position:absolute;top:494px;left:539px;width:108px;height:36px}
.tabs{position:absolute;top:551px;left:327px;display:flex;gap:16px}
.tab{height:44px;display:flex;align-items:center;justify-content:center;background:#f6f7f8;font-size:18px;font-weight:500;color:#333}
.tab.active{background:var(--blue);color:var(--white)}
.integration-visual{position:absolute;left:58px;top:660px;width:482px;height:240px;border-radius:120px;
  background:radial-gradient(ellipse at 72% 50%,#2271ab 0%,#3a86bd 40%,rgba(222,240,246,0) 72%),radial-gradient(ellipse at 25% 50%,#ffffff 0%,rgba(255,255,255,.6) 45%,rgba(222,240,246,0) 72%)}
.feature{position:absolute;left:646px;top:622px;width:410px}
.feature h2{font-size:25px;font-weight:400;color:#444}
.feature h3{font-size:16px;font-weight:700;color:var(--blue);line-height:18px;margin-top:14px;width:340px}
.feature ul{list-style:none;margin-top:16px;width:382px}
.feature li{font-size:13px;line-height:19px;color:#555;padding-left:20px;position:relative;margin-bottom:10px}
.feature li::before{content:"";position:absolute;left:2px;top:4px;width:8px;height:4px;border-left:2px solid var(--blue);border-bottom:2px solid var(--blue);transform:rotate(-45deg)}
.feature p{font-size:13px;line-height:19.5px;color:#555;margin-top:14px;width:400px}

/* like strip */
.likebar{height:89px;background:#f6f7f8}
.likebar .line{position:absolute;left:0;right:0;top:44px;border-top:1px solid #e2e4e7}
.like-pill{position:absolute;left:376px;top:21px;width:447px;height:44px;border:1px solid #e2e4e7;border-radius:22px;background:var(--white);display:flex;align-items:center;gap:10px;padding-left:120px;font-size:11px;color:#333}
.like-pill .thumbcirc{position:absolute;left:0;top:0;width:60px;height:42px;border-right:1px solid #e2e4e7;border-radius:22px 0 0 22px}
.like-btn{background:#4a6fb5;color:var(--white);font-weight:700;font-size:10px;padding:3px 7px;border-radius:2px}

/* footer */
.footer{height:114px;background:var(--blue-dark);color:var(--white)}
.footer-nav{position:absolute;left:23px;top:20px;display:flex;gap:33px;font-size:13px;font-weight:500;letter-spacing:.5px}
.footer-address{position:absolute;left:23px;top:53px;font-size:12px;color:rgba(255,255,255,.75)}
.footer-legal{position:absolute;left:23px;top:85px;display:flex;font-size:10px;color:rgba(255,255,255,.75)}
.footer-legal span{padding:0 16px;border-left:1px solid rgba(255,255,255,.4)}
.footer-legal span:first-child{padding-left:0;border-left:none}
.footer-social{position:absolute;right:17px;top:9px;display:flex;gap:10px}
.footer-social i{width:36px;height:36px;background:#1f2d3a;display:block}
.copyright{position:absolute;right:17px;top:74px;font-size:12px;color:rgba(255,255,255,.75)}
</style>
</head>
<body>

<header>
  <div class="topbar">
    <div class="contact">
      <span><svg width="11" height="11" viewBox="0 0 24 24"><path fill="#fff" d="M6.6 10.8a15 15 0 0 0 6.6 6.6l2.2-2.2c.3-.3.7-.4 1-.2 1.1.4 2.3.6 3.6.6.6 0 1 .4 1 1V20c0 .6-.4 1-1 1A17 17 0 0 1 3 4c0-.6.4-1 1-1h3.5c.6 0 1 .4 1 1 0 1.3.2 2.5.6 3.6.1.3 0 .7-.2 1z"/></svg>+1 800 555 01 42</span>
      <span><svg width="13" height="10" viewBox="0 0 26 20"><rect x="1" y="1" width="24" height="18" fill="none" stroke="#fff" stroke-width="2"/><path d="M1 1l12 10L25 1" fill="none" stroke="#fff" stroke-width="2"/></svg>info@brightkestrel.com</span>
    </div>
    <div class="right">
      <i class="social-dot"></i><i class="social-dot"></i><i class="social-dot"></i>
      <span>Login</span>
      <svg width="13" height="13" viewBox="0 0 20 20"><circle cx="8" cy="8" r="6" fill="none" stroke="#fff" stroke-width="2.5"/><path d="M12.5 12.5L18 18" stroke="#fff" stroke-width="2.5"/></svg>
    </div>
  </div>
  <nav class="navbar">
    <div class="brand">BrightKestrel</div>
    <div class="menu"><span>Product</span><span>About</span><span>Resources</span><span>Pricing</span><span>Blog</span><span>Contact</span></div>
  </nav>
</header>

<section class="hero">
  <div class="globe" role="img" aria-label="Glowing wireframe globe of connected network points"></div>
  <div class="hero-copy">
    <h1 class="hero-title">Cloud Infrastructure<br>Security for NBX</h1>
    <p class="hero-sub">Security and Compliance Automation - Built For Modern IT</p>
    <div class="hero-actions">
      <span class="btn btn-primary">Get Started</span>
      <span class="btn btn-ghost">Go on surfing</span>
      <span class="badge" role="img" aria-label="Partner badge"></span>
    </div>
  </div>
</section>

<section class="about" role="img" aria-label="Light network mesh background">
  <h2 class="section-title">Who are we?</h2>
  <div class="rule"></div>
  <p>Our company is called BrightKestrel and our purpose is to help companies sustainably embrace and reap the benefits of cloud platforms, through transforming practices, skills and technology using DevOps and Security practices such that they are able to automate, manage and secure their cloud platforms to deliver product to market with increasing velocity.</p>
</section>

<section class="services">
  <h2 class="section-title">Services</h2>
  <div class="rule"></div>
  <div class="service" style="left:24px">
    <div class="icon"><svg width="38" height="38" viewBox="0 0 40 40" fill="none" stroke="#fff" stroke-width="2.2" stroke-linejoin="round"><rect x="4" y="17" width="7" height="18"/><path d="M11 19l7-10c1-2 4-1 4 1v6h10c2 0 3 2 2.5 3.5L32 33c-.4 1.3-1.5 2-3 2H11"/></svg></div>
    <h3>Automated</h3>
    <p>Continuous security assessment of all NBX Cloud helps you to identify risk and meet requirements of the shared responsibility model.</p>
  </div>
  <div class="service" style="left:400px">
    <div class="icon"><svg width="30" height="44" viewBox="0 0 30 44" fill="none" stroke="#fff" stroke-width="2.2" stroke-linejoin="round"><path d="M15 2c7 6 8 16 5 26H10C7 18 8 8 15 2z"/><circle cx="15" cy="14" r="3"/><path d="M10 24l-6 7v4l6-3M20 24l6 7v4l-6-3M12 32l3 8 3-8"/></svg></div>
    <h3>End-to-end</h3>
    <p>End-to-end infrastructure visibility vs. tactical, agent-based implementation virtually guarantees manageability and effortless scalability.</p>
  </div>
  <div class="service" style="left:774px">
    <div class="icon"><svg width="30" height="38" viewBox="0 0 30 38" fill="none" stroke="#fff" stroke-width="2"><path d="M3 2h17l7 7v27H3z"/><path d="M20 2v7h7M8 16h14M8 22h14M8 28h14"/></svg></div>
    <h3>Easy Integration</h3>
    <p>Simple, fast, and effective integration with the leading DevOps tools for increased visibility and response to security issues.</p>
  </div>
</section>

<section class="blog">
  <h2 class="section-title">Blog</h2>
  <div class="rule"></div>
  <div class="cards">
    <article class="card"><div class="thumb">270x200</div><div class="body"><h4>Ullamcorper Parturien</h4><p>Morbi leo risus, porta ac consectur at eros. Maecenas sed diam eget risus varius blandit sit amet non.</p><div class="meta"><span>28 October, 2020</span><span>15</span></div></div></article>
    <article class="card"><div class="thumb">270x200</div><div class="body"><h4>Excepteur Sint Occaecat</h4><p>Lorem ipsum dolor sit amet, consectetur adipiscing elit, sed do eiusmod tempor incididunt ut lab.</p><div class="meta"><span>27 October, 2020</span><span>11</span></div></div></article>
    <article class="card"><div class="thumb">270x200</div><div class="body"><h4>Neque Porro Quisquam</h4><p>Sed ut perspiciatis unde omnis iste natus error sit voluptatem accusantium doloremque laudanti.</p><div class="meta"><span>26 October, 2020</span><span>10</span></div></div></article>
    <article class="card"><div class="thumb">270x200</div><div class="body"><h4>Quis Autem Vel Eum</h4><p>Nemo enim ipsam voluptatem quia voluptas sit aspernatur aut odit aut fugit, sed quia consetur.</p><div class="meta"><span>25 October, 2020</span><span>15</span></div></div></article>
  </div>
  <span class="btn btn-primary view-more">View more</span>

  <div class="tabs">
    <span class="tab active" style="width:154px">For Modern IT</span>
    <span class="tab" style="width:227px">For Risk &amp; Compliance</span>
    <span class="tab" style="width:135px">For DevOps</span>
  </div>

  <div class="integration-visual" role="img" aria-label="Illustration of integrated tools around a cloud hub, linked to a DevOps cycle wheel: develop, test, deploy to staging, security check, deploy to production"></div>

  <div class="feature">
    <h2>Native NBX Security for Modern IT</h2>
    <h3>Accelerate Workload Migration with Security Automation</h3>
    <ul>
      <li>Agentless, Non-intrusive Deployment in Minutes</li>
      <li>Continuously Identify Risk Across All NBX Accounts, Regions and Services</li>
      <li>Rapidly Mitigate Risk with Step-by-Step, Guided Remediation</li>
      <li>Integrates with SIEM and Other Solutions via Direct and Custom API Integration</li>
    </ul>
    <p>Lorem ipsum dolor sit amet, consectetur adipiscing elit, sed do eiusmod tempor incididunt ut labore et dolore magna aliqua. Ut enim ad minim veniam, quis nostrud exercitation ullamco laboris nisi ut aliquip ex ea commodo consequat.</p>
  </div>
</section>

<section class="likebar">
  <div class="line"></div>
  <div class="like-pill"><span class="thumbcirc"></span><span class="like-btn">Like</span><span>You and 4.1k others like this.</span></div>
</section>

<footer class="footer">
  <div class="footer-nav"><span>PRODUCT</span><span>ABOUT</span><span>RESOURCES</span><span>PRICING</span><span>LOGIN</span></div>
  <div class="footer-address">412 Harbour Lane, Sydney | sales@BrightKestrel.com | support@BrightKestrel.com</div>
  <div class="footer-legal"><span>Security</span><span>Privacy</span><span>Terms of Service</span></div>
  <div class="footer-social"><i></i><i></i><i></i><i></i></div>
  <div class="copyright">Copyright © 2016 BrightKestrel All rights reserved.</div>
</footer>

</body>
</html>
```